Web API Startup Need Wordpress site

Company Logo and color scheme are completed. Now we want to use Wordpress to publish the company overview, team members, products, press releases, a blog, contact us.

This company is a startup so we want to be smart, edgy and fun. This company's goal is to kick over some trash can's in healthcare, government, and enterprise IT web applications so we have to be professional while we challenge the status quo.

We want to use a Bootstrap theme, if possible.

Target Market(s)

Professionals and Enterprise customers looking to use the services of a web api company. This could be doctors, journalists, enterprise it departments.

Industry/Entity Type

Information Technology

Coding

Coded - Design and coding required

Font styles to use
Sans Serif

Requirements
Must have
• a portfolio view to display products, which are web applications, a page for press releases, a page for blogs, company overview and team members, places to embed videos
Nice to have
• One idea could be to have a great hero image that captures clouds, water, green grass, an individual (like the symbols in the logo);
• Great use of color is important so that the site is cool, edgy but fun tech

```html
<!DOCTYPE html>
<html lang="en">
<head>
<meta charset="utf-8">
<title>Brightcask — Web Applications</title>
<link href="https://fonts.googleapis.com/css2?family=Lato:wght@400;700;900&display=swap" rel="stylesheet">
<style>
:root{
  --green:#6bb04a;
  --navy:#3e5a85;
  --blue:#1e95d2;
  --ink:#2b2b2b;
  --text:#666;
  --muted:#999;
  --light:#efefef;
  --line:#e2e2e2;
  --circuit:#cfe5f4;
  --white:#fff;
}
*{box-sizing:border-box;margin:0;padding:0}
html,body{width:1200px;height:3163px;overflow:hidden}
body{font-family:'Lato',sans-serif;color:var(--text);background:var(--white);position:relative}
.abs{position:absolute}
a{color:inherit;text-decoration:none}

.topbar{left:0;top:0;width:1200px;height:30px;background:var(--green);color:var(--white);font-size:11px}
.topbar .links{left:93px;top:8px;display:flex;gap:8px}
.topbar .links span.sep{opacity:.6}
.topbar .right{right:93px;top:7px;display:flex;gap:12px;align-items:center}
.topbar .dot{width:11px;height:11px;border-radius:50%;background:var(--white);opacity:.9}

.header{left:0;top:30px;width:1200px;height:145px}
.brand{left:0;top:0;width:1200px;height:145px;display:flex;align-items:center;justify-content:center;gap:12px}
.brand .mark{width:34px;height:34px;border-radius:50%;background:var(--blue)}
.brand .name{font-weight:900;font-size:30px;letter-spacing:2px;color:var(--navy)}

.nav{left:0;top:175px;width:1200px;height:36px;background:var(--navy);color:var(--white);font-size:10.5px;font-weight:700;letter-spacing:.5px;display:flex;justify-content:center;align-items:center;gap:26px}

.hero .tile{display:flex;align-items:flex-end;justify-content:center;color:var(--white);font-size:14px;font-weight:700;letter-spacing:2px;text-align:center;padding-bottom:30px}
.tile-lab{left:0;top:211px;width:600px;height:483px;background:linear-gradient(135deg,#9fc3de,#6e9fc8 60%,#8fb7d8)}
.tile-mag{left:600px;top:211px;width:600px;height:242px;background:linear-gradient(180deg,#1c6fbf,#3a8fd8 55%,#8ec4ee);align-items:center!important;padding-bottom:0!important}
.tile-gov{left:600px;top:453px;width:300px;height:241px;background:linear-gradient(135deg,#7fa9cf,#5e8fbd)}
.tile-hc{left:900px;top:453px;width:300px;height:241px;background:linear-gradient(135deg,#a9d3ec,#7dbde3)}

.features{left:0;top:694px;width:1200px;height:281px}
.feature{top:50px;width:300px;text-align:center}
.feature .icon{width:56px;height:56px;margin:0 auto 18px;border:2px solid var(--navy);border-radius:50%;display:flex;align-items:center;justify-content:center}
.feature h3{font-size:14px;font-weight:900;color:var(--ink);letter-spacing:1px;margin-bottom:8px}
.feature p{font-size:13px;line-height:20px}
.vdiv{top:30px;width:1px;height:250px;background:var(--line)}

.totop{width:34px;height:34px;border-radius:50%;border:1.5px solid #555;display:flex;align-items:center;justify-content:center}
.totop.faint{border-color:#ccc}

.circuit{left:0;top:1002px;width:1200px;height:350px;background:var(--circuit)}
.circuit-box{left:190px;top:1124px;width:823px;height:95px;background:var(--green);color:var(--white);text-align:center;box-shadow:0 4px 10px rgba(0,0,0,.15)}
.circuit-box h2{font-weight:400;font-size:30px;margin-top:6px}
.circuit-box p{font-size:13px;line-height:20px;margin-top:4px;padding:0 20px}

.photo{box-shadow:0 3px 8px rgba(0,0,0,.15)}
.photo-devices{left:93px;top:1411px;width:479px;height:335px;background:radial-gradient(circle at 50% 40%,#4fa8ff,#0b3fa8 70%,#072a72)}
.photo-digital{left:629px;top:1892px;width:478px;height:301px;background:linear-gradient(135deg,#6e9fd8,#2f66b8 55%,#9fd0f2)}
.split h2{font-size:22px;font-weight:700;letter-spacing:2px;color:var(--ink);margin-bottom:16px}
.split p{font-size:14px;line-height:24px;width:478px}
.hline{left:0;top:1831px;width:1200px;height:1px;background:var(--line)}

.news{left:0;top:2278px;width:1200px;height:358px;background:var(--light)}
.news-intro{left:93px;top:2323px;width:230px}
.news-intro h2{font-size:17px;font-weight:700;letter-spacing:1.5px;color:var(--ink);margin-bottom:8px}
.news-intro p{font-size:13px;line-height:22px}
.post{top:2322px;height:215px;background:var(--white);box-shadow:0 2px 6px rgba(0,0,0,.1);display:flex}
.post .thumb{width:148px;height:100%;background:#e4e8ee;position:relative}
.post .date{position:absolute;left:6px;top:17px;width:30px;height:38px;background:var(--white);border:1px solid #ccc;text-align:center;font-size:13px;font-weight:700;color:var(--ink);line-height:18px}
.post .date small{display:block;font-size:8px;font-weight:400;border-top:1px solid #ccc;line-height:14px}
.post .body{padding:34px 20px 0 20px;flex:1}
.post h4{font-size:11px;font-weight:700;color:var(--ink);margin-bottom:14px}
.post p{font-size:12px;line-height:19px}

.callout{left:0;top:2636px;width:1200px;height:158px;background:var(--blue);color:var(--white)}
.callout h2{position:absolute;left:93px;top:43px;font-size:26px;font-weight:700;letter-spacing:1px}
.callout p{position:absolute;left:93px;top:84px;width:560px;font-size:14px;line-height:23px}

.footer{left:0;top:2794px;width:1200px;height:312px;background:var(--green);color:var(--white)}
.fcol{top:30px}
.fcol h3{font-size:13px;font-weight:700;letter-spacing:1.5px;margin-bottom:20px}
.fcol p{font-size:13px;line-height:21px}
.recent li{list-style:none;display:flex;gap:10px;margin-bottom:16px;font-size:14px}
.recent .d{width:30px;height:34px;border:1px solid rgba(255,255,255,.8);font-size:11px;text-align:center;line-height:16px;font-weight:700}
.recent .d small{display:block;font-size:7px;font-weight:400}
.recent em{font-style:normal;display:block;font-size:9px;opacity:.8}
.tags{font-size:10px;line-height:22px;width:230px}
.cal{left:875px;top:2828px;width:243px;font-size:13px;text-align:center}
.cal caption{padding-bottom:6px}
.cal table{width:100%;border-collapse:collapse}
.cal td,.cal th{height:32px;font-weight:400}
.cal .prev{text-align:left;margin-top:2px}

.bottombar{left:0;top:3106px;width:1200px;height:57px;background:var(--navy);color:#aebbd1;font-size:11px;letter-spacing:1px;display:flex;justify-content:center;align-items:center;gap:18px}
</style>
</head>
<body>

<div class="abs topbar">
  <div class="abs links"><a>Blog</a><span class="sep">|</span><a>Our Story</a><span class="sep">|</span><a>Support</a><span class="sep">|</span><a>FAQ</a></div>
  <div class="abs right">
    <span style="display:flex;align-items:center;gap:5px">
      <svg width="13" height="10" viewBox="0 0 13 10"><rect x=".5" y=".5" width="12" height="9" fill="none" stroke="#fff"/><path d="M.5 .5l6 5 6-5" fill="none" stroke="#fff"/></svg>
      Newsletter Signup</span>
    <span class="dot"></span><span class="dot"></span><span class="dot"></span><span class="dot"></span>
  </div>
</div>

<header class="abs header">
  <div class="abs brand"><span class="mark"></span><span class="name">BRIGHTCASK</span></div>
</header>

<nav class="abs nav">
  <a>OUR STORY</a><a>MEET THE TEAM</a><a>PORTFOLIO ⌄</a><a>BLOG</a><a>PRESS RELEASES</a><a>CONTACT US</a>
  <svg width="12" height="12" viewBox="0 0 12 12"><circle cx="5" cy="5" r="3.8" fill="none" stroke="#fff" stroke-width="1.6"/><path d="M8 8l3 3" stroke="#fff" stroke-width="1.8"/></svg>
</nav>

<section class="hero">
  <div class="abs tile tile-lab" role="img" aria-label="Photo of a scientist working with lab equipment, blue tint">HEALTHCARE EXPERT APPLICATION</div>
  <div class="abs tile tile-mag" role="img" aria-label="Photo of a glass skyscraper seen from below, blue tint">ENTERPRISE MAGAZINE APPLICATION</div>
  <div class="abs tile tile-gov" role="img" aria-label="Photo of a microscope, blue tint">GOVERNMENT APPLICATION</div>
  <div class="abs tile tile-hc" role="img" aria-label="Photo of a person stretching, light blue tint">HEALTHCARE WEB<br>APPLICATION</div>
</section>

<section class="abs features">
  <div class="abs feature" style="left:150px">
    <div class="icon"><svg width="26" height="22" viewBox="0 0 26 22"><path d="M2 21h22M5 21V12M10 21V7M15 21V10M20 21V4" stroke="#6bb04a" stroke-width="3"/></svg></div>
    <h3>ENTERPRISE WEB APPLICATIONS</h3>
    <p>Enterprise Lorem ipsum dolor sit amet, consectetuer adipiscing elit, sed diam nonummy nibh euismod tincidunt ut laoreet dolore magna aliquam erat volutpat….</p>
  </div>
  <div class="abs vdiv" style="left:422px"></div>
  <div class="abs feature" style="left:451px">
    <div class="icon"><svg width="22" height="24" viewBox="0 0 22 24"><path d="M11 1l4 5H7zM6 7h10v15H6zM2 22h18" fill="#6bb04a" stroke="#6bb04a" stroke-width="1.5"/><path d="M9 11v9M13 11v9" stroke="#fff" stroke-width="1.5"/></svg></div>
    <h3>GOVERMENT WEB APPLICATION</h3>
    <p>Goverment Web Application Lorem ipsum dolor sit amet, consectetuer adipiscing elit, sed diam nonummy nibh euismod tincidunt ut laoreet dolore magna aliquam erat volutpat….</p>
  </div>
  <div class="abs vdiv" style="left:780px"></div>
  <div class="abs feature" style="left:810px">
    <div class="icon"><svg width="24" height="22" viewBox="0 0 24 22"><path d="M12 20S2 13.5 2 7.5A5 5 0 0 1 12 5a5 5 0 0 1 10 2.5C22 13.5 12 20 12 20z" fill="none" stroke="#6bb04a" stroke-width="2.2"/></svg></div>
    <h3>HEALTHCARE WEB APPLICATIONS</h3>
    <p>Healthcare Web Applications Lorem ipsum dolor sit amet, consectetuer adipiscing elit, sed diam nonummy nibh euismod tincidunt ut laoreet dolore magna aliquam erat volutpat….</p>
  </div>
  <div class="abs totop faint" style="left:1142px;top:110px"><svg width="12" height="8" viewBox="0 0 12 8"><path d="M1 7l5-5 5 5" fill="none" stroke="#ccc" stroke-width="1.5"/></svg></div>
</section>

<section>
  <div class="abs circuit" role="img" aria-label="Light blue circuit board pattern background"></div>
  <div class="abs totop" style="left:1142px;top:1087px"><svg width="12" height="8" viewBox="0 0 12 8"><path d="M1 7l5-5 5 5" fill="none" stroke="#555" stroke-width="1.5"/></svg></div>
  <div class="abs circuit-box">
    <h2>We {DEVELOP} the future</h2>
    <p>lorem ipsum dolor sit amet, consectetuer adipiscing elit, sed diam nonummy nibh euismod tincidunt ut laoreet dolore magna aliquam erat volutpat.</p>
  </div>
</section>

<section class="split">
  <div class="abs totop" style="left:1142px;top:1376px"><svg width="12" height="8" viewBox="0 0 12 8"><path d="M1 7l5-5 5 5" fill="none" stroke="#555" stroke-width="1.5"/></svg></div>
  <div class="abs photo photo-devices" role="img" aria-label="Hand holding a phone in front of tablets with glowing digital network"></div>
  <div class="abs" style="left:629px;top:1510px">
    <h2>SECTION WITH IMAGE LEFT</h2>
    <p>Lorem ipsum dolor sit amet, consectetuer adipiscing elit, sed diam nonummy nibh euismod tincidunt ut laoreet dolore magna aliquam erat volutpat.</p>
  </div>
  <div class="abs totop" style="left:1142px;top:1664px"><svg width="12" height="8" viewBox="0 0 12 8"><path d="M1 7l5-5 5 5" fill="none" stroke="#555" stroke-width="1.5"/></svg></div>
  <div class="abs hline"></div>

  <div class="abs" style="left:93px;top:1975px">
    <h2>SECTION WITH IMAGE RIGHT</h2>
    <p>Lorem ipsum dolor sit amet, consectetuer adipiscing elit, sed diam nonummy nibh euismod tincidunt ut laoreet dolore magna aliquam erat volutpat.</p>
  </div>
  <div class="abs photo photo-digital" role="img" aria-label="Blue digital portrait overlaid with binary code"></div>
  <div class="abs totop" style="left:1142px;top:1954px"><svg width="12" height="8" viewBox="0 0 12 8"><path d="M1 7l5-5 5 5" fill="none" stroke="#555" stroke-width="1.5"/></svg></div>
  <div class="abs totop" style="left:1142px;top:2242px"><svg width="12" height="8" viewBox="0 0 12 8"><path d="M1 7l5-5 5 5" fill="none" stroke="#555" stroke-width="1.5"/></svg></div>
</section>

<section class="abs news"></section>
<div class="abs news-intro">
  <h2>LATEST NEWS</h2>
  <p>Lorem ipsum dolor sit amet, consectetuer adipiscing elit, sed diam nonummy nibh euismod .</p>
</div>
<article class="abs post" style="left:352px;width:359px">
  <div class="thumb"><div class="date">13<small>Oct</small></div></div>
  <div class="body"><h4>A Simple Blog Post</h4><p>Lorem ipsum dolor sit amet, consectetuer adipiscing elit, sed diam nonummy nibh euismod tincidunt ut [...]</p></div>
</article>
<article class="abs post" style="left:745px;width:362px">
  <div class="thumb"><div class="date">16<small>Dec</small></div></div>
  <div class="body"><h4>Another post with A Gallery</h4><p>Lorem ipsum dolor sit amet, consectetuer adipiscing elit. In sed vulputate massa. Fusce ante magna [...]</p></div>
</article>
<div class="abs totop" style="left:1142px;top:2528px"><svg width="12" height="8" viewBox="0 0 12 8"><path d="M1 7l5-5 5 5" fill="none" stroke="#555" stroke-width="1.5"/></svg></div>

<section class="abs callout">
  <h2>ADD A CALLOUT HEADER HERE</h2>
  <p>Lorem ipsum dolor sit amet, consectetuer adipiscing elit, sed diam nonummy nibh euismod tincidunt ut laoreet dolore magna aliquam erat volutpat.</p>
</section>

<footer class="abs footer">
  <div class="abs fcol" style="left:93px;width:230px">
    <h3>SIGNUP FOR NEWSLETTER</h3>
    <p>Lorem ipsum dolor sit amet, consectetuer adipiscing elit, sed diam nonummy nibh euismod tincidunt ut laoreet.</p>
    <p style="margin-top:14px">(insert contact form here)</p>
  </div>
  <div class="abs fcol" style="left:354px;width:230px">
    <h3>RECENT POSTS</h3>
    <ul class="recent">
      <li><span class="d">14<small>Nov</small></span><span>Hello world!<em>1 Comment</em></span></li>
      <li><span class="d">19<small>Nov</small></span><span>Welcome to Lumenfold</span></li>
      <li><span class="d">13<small>Oct</small></span><span>Just another post with A Gallery</span></li>
    </ul>
  </div>
  <div class="abs fcol" style="left:614px">
    <h3>TAGS</h3>
    <p class="tags">Enterprise Government Healthcare Web Applications</p>
  </div>
  <div class="abs totop" style="left:1142px;top:40px;border-color:rgba(255,255,255,.6)"><svg width="12" height="8" viewBox="0 0 12 8"><path d="M1 7l5-5 5 5" fill="none" stroke="#fff" stroke-width="1.5"/></svg></div>
</footer>
<div class="abs cal" style="color:#fff">
  <table>
    <caption>November 2016</caption>
    <tr><th>M</th><th>T</th><th>W</th><th>T</th><th>F</th><th>S</th><th>S</th></tr>
    <tr><td></td><td>1</td><td>2</td><td>3</td><td>4</td><td>5</td><td>6</td></tr>
    <tr><td>7</td><td>8</td><td>9</td><td>10</td><td>11</td><td>12</td><td>13</td></tr>
    <tr><td>14</td><td>15</td><td>16</td><td>17</td><td>18</td><td>19</td><td>20</td></tr>
    <tr><td>21</td><td>22</td><td>23</td><td>24</td><td>25</td><td>26</td><td>27</td></tr>
    <tr><td>28</td><td>29</td><td>30</td><td></td><td></td><td></td><td></td></tr>
  </table>
  <div class="prev">« Nov</div>
</div>

<div class="abs bottombar"><a>BLOG</a><a>OUR STORY</a><a>SUPPORT</a><a>FAQ</a></div>
<div class="abs totop faint" style="left:1142px;top:3117px;border-color:#5c7499"></div>

</body>
</html>
```